Animal Hospital Business Cards

Make a business card look like the attached example

*Use the same blue/black coloring
*Brisket Hollow Animal Hospital (instead of pet home rounds)
*Emergency Services (instead of tamsin creek clinic)
*House Calls (instead of open 7 days by appointment)
*Change address to 278 Brisket Hollow Rd Loveland, OH 45263
*Open 7 days a week (instead of emergency service)
*Add the website www.briskethollowanimalhospital.example

On the back...
*instead of the text outlined in red, just white
*instead of the light blue, try your best to make it just like the blue and black on the front side of the card
*Delete "designed and printed by 9 whiskers inc, www.pressfeline.example

Requirements
Must have
• look just like the attached example with requested edits/changes

```html
<!DOCTYPE html>
<html lang="en">
<head>
<meta charset="utf-8">
<title>Brisket Hollow Animal Hospital – Business Card</title>
<link href="https://fonts.googleapis.com/css2?family=Arimo:ital,wght@0,400;0,700;1,700&family=Oswald:wght@500;600&display=swap" rel="stylesheet">
<style>
  :root {
    --blue: #3a87c8;
    --blue-deep: #17668f;
    --edge: #0e2a38;
    --black: #000;
    --grey: #d4d4d4;
    --red: #9b1c1f;
    --ink: #000;
    --label-blue: #1a6596;
    --white: #fff;
    --mon: #a8475f; --tue: #d8702f; --wed: #527f9d; --thu: #a91f27;
    --fri: #b39a32; --sat: #9c4255; --sun: #1d5531;
  }
  * { box-sizing: border-box; margin: 0; padding: 0; }
  html, body { width: 1200px; height: 900px; overflow: hidden; background: var(--white); }
  body { position: relative; font-family: "Arimo", Arial, sans-serif; }

  .card { position: absolute; left: 381px; width: 532px; height: 325px; border-radius: 28px; overflow: hidden; background: var(--white); }
  .card--front { top: 67px; }
  .card--back { top: 489px; border: 2px solid var(--grey); }
  .card__bands { position: absolute; inset: 0; }
  .abs { position: absolute; left: 0; width: 100%; text-align: center; white-space: nowrap; }

  .front__title { top: 10px; font-family: "Oswald", sans-serif; font-weight: 500; font-size: 27px; color: var(--white); letter-spacing: 0.5px; }
  .front__doctor { top: 80px; font-weight: 700; font-size: 22px; color: var(--ink); }
  .front__side { position: absolute; top: 140px; width: 140px; text-align: center; font-weight: 700; font-size: 19px; line-height: 23px; color: var(--ink); }
  .front__side--left { left: 8px; }
  .front__side--right { right: 0; }
  .front__mark { top: 122px; display: flex; justify-content: center; align-items: center; gap: 6px; font-weight: 700; font-size: 14px; color: var(--red); }
  .front__mark-dot { width: 12px; height: 12px; border-radius: 50%; background: var(--red); }
  .front__species { top: 168px; font-weight: 700; font-style: italic; font-size: 16px; color: var(--ink); }
  .front__phone { top: 190px; font-weight: 700; font-size: 35px; color: var(--red); }
  .front__address { top: 234px; font-weight: 700; font-size: 13.5px; color: var(--red); }
  .front__web { left: 95px; width: 362px; top: 278px; font-weight: 700; font-size: 16px; letter-spacing: -0.3px; color: var(--white); }
  .front__web-alt { left: 95px; width: 362px; top: 300px; font-weight: 700; font-size: 14px; color: var(--white); }
  .badge-open { position: absolute; left: 43px; top: 266px; width: 44px; height: 48px; border: 2px solid var(--white); border-radius: 3px; color: var(--white); font-weight: 700; text-align: center; line-height: 11px; padding-top: 6px; font-size: 12px; }
  .badge-open small { font-size: 9px; }
  .badge-years { position: absolute; left: 466px; top: 266px; width: 46px; height: 46px; border-radius: 50%; border: 2px dashed var(--white); background: var(--black); color: var(--white); text-align: center; font-weight: 700; line-height: 1; padding-top: 5px; }
  .badge-years b { display: block; font-size: 17px; }
  .badge-years span { display: block; font-size: 8px; }
  .badge-years em { display: block; font-size: 4px; font-style: normal; }

  .back__head { position: absolute; top: 0; left: 0; width: 100%; height: 117px; background: var(--blue-deep); }
  .back__title { top: 8px; font-family: "Oswald", sans-serif; font-weight: 600; font-size: 34px; line-height: 44px; color: var(--white); }
  .back__doctor { top: 58px; font-weight: 700; font-size: 22px; color: var(--white); }
  .back__phone { top: 88px; font-weight: 700; font-size: 22px; color: var(--red); letter-spacing: 1px; }
  .back__line { position: absolute; font-family: "Oswald", sans-serif; font-weight: 500; color: var(--label-blue); font-size: 21px; line-height: 28px; white-space: nowrap; }
  .blank { display: inline-block; height: 20px; border-bottom: 2px solid var(--label-blue); vertical-align: baseline; margin: 0 4px; }
  .back__for { left: 33px; top: 128px; }
  .back__for .blank { width: 208px; }
  .back__date { left: 26px; top: 258px; }
  .back__date .blank { width: 160px; }
  .back__time { left: 256px; top: 258px; }
  .back__time .blank { width: 160px; }
  .back__ampm { left: 477px; top: 250px; font-size: 15px; line-height: 19px; }
  .days { position: absolute; top: 188px; left: 0; width: 100%; height: 44px; }
  .day { position: absolute; width: 56px; height: 44px; border-radius: 14px; color: #e6d9dc; font-family: "Oswald", sans-serif; font-weight: 500; font-size: 16px; display: flex; align-items: center; justify-content: center; }
</style>
</head>
<body>

<section class="card card--front" aria-label="Business card front">
  <svg class="card__bands" width="532" height="325" viewBox="0 0 532 325" aria-hidden="true">
    <defs>
      <linearGradient id="bandBlue" x1="0" x2="1" y1="0" y2="0">
        <stop offset="0" stop-color="#0e2a38"/>
        <stop offset="0.25" stop-color="#3a87c8"/>
        <stop offset="0.75" stop-color="#3a87c8"/>
        <stop offset="1" stop-color="#0e2a38"/>
      </linearGradient>
    </defs>
    <polygon points="0,0 532,0 532,62 0,42" fill="url(#bandBlue)"/>
    <polygon points="0,42 532,62 532,64 0,64" fill="#000"/>
    <polygon points="0,64 532,64 532,70 0,76" fill="#d4d4d4"/>
    <polygon points="0,255 532,250 532,262 0,258" fill="#d4d4d4"/>
    <polygon points="0,258 532,262 532,285 0,260" fill="#000"/>
    <polygon points="0,260 532,285 532,325 0,325" fill="url(#bandBlue)"/>
  </svg>
  <h1 class="abs front__title">BRISKET HOLLOW ANIMAL HOSPITAL</h1>
  <p class="abs front__doctor">Harlan P. Whitcombe, DVM</p>
  <p class="front__side front__side--left">Emergency<br>Services</p>
  <p class="front__side front__side--right">House<br>Calls</p>
  <div class="abs front__mark"><span class="front__mark-dot"></span>Brisket Hollow</div>
  <p class="abs front__species">Cats • Dogs • Birds • Exotics</p>
  <p class="abs front__phone">(513) 555-0147</p>
  <p class="abs front__address">278 Brisket Hollow Rd Loveland, OH 45263</p>
  <div class="badge-open">OPEN<br>7 <small>days</small><br><small>a week</small></div>
  <p class="abs front__web">www.briskethollowanimalhospital.example</p>
  <p class="abs front__web-alt">www.tamsincreekvet.example</p>
  <div class="badge-years"><b>30</b><span>years</span><em>of Experience</em></div>
</section>

<section class="card card--back" aria-label="Appointment card back">
  <div class="back__head"></div>
  <h2 class="abs back__title">Veterinary Appointment</h2>
  <p class="abs back__doctor">Harlan P. Whitcombe, DVM</p>
  <p class="abs back__phone">513.555.0147</p>
  <p class="back__line back__for">Your appointment for<span class="blank"></span>is on</p>
  <div class="days">
    <span class="day" style="left:18px;background:var(--mon)">Mon</span>
    <span class="day" style="left:87px;background:var(--tue)">Tues</span>
    <span class="day" style="left:163px;background:var(--wed)">Wed</span>
    <span class="day" style="left:240px;background:var(--thu)">Thur</span>
    <span class="day" style="left:314px;background:var(--fri)">Fri</span>
    <span class="day" style="left:390px;background:var(--sat)">Sat</span>
    <span class="day" style="left:456px;background:var(--sun)">Sun</span>
  </div>
  <p class="back__line back__date">Date<span class="blank"></span></p>
  <p class="back__line back__time">Time<span class="blank"></span></p>
  <p class="back__line back__ampm">AM<br>PM</p>
</section>

</body>
</html>
```